Business Card Design Project

This is a new division in our company. "Meridale Wellsite & Safety" This is a Oilfield Safety company. I have included our new logo. I also have given our other business card. We love double sided with lots of color. We like to stand out. Please DO NOT duplicate our other card and bring your design into it. See all attached files.
Reason: forgot to change this when I posted it.
Here is the correct information card.
www.meridalewellsitesafety.com
Dwayne@meridalewellsitesafety.com
Reason: revision for a few.
Reason: was traveling and need to review designs.
Oil and Gas industry. Masculine look.
Business

```html
<!DOCTYPE html>
<html lang="en">
<head>
<meta charset="utf-8">
<title>Meridale Wellsite &amp; Safety — Business Card</title>
<link rel="stylesheet" href="https://fonts.googleapis.com/css2?family=Michroma&family=Roboto+Condensed:wght@400&display=swap">
<style>
  :root {
    --backdrop: #939393;
    --card: #ffffff;
    --orange: #ef5a2f;
    --green: #82c341;
    --teal: #2bb7b3;
    --teal-light: #7fd3d0;
    --yellow: #e8e04a;
    --ink: #4a4a4a;
  }
  html, body {
    margin: 0;
    width: 1200px;
    height: 1000px;
    overflow: hidden;
    background: var(--backdrop);
  }
  .canvas { position: relative; width: 1200px; height: 1000px; }
  .card {
    position: absolute;
    width: 543px;
    height: 318px;
    background: var(--card);
    overflow: hidden;
  }
  .card--back { left: 123px; top: 128px; }
  .card--front { left: 518px; top: 530px; }
  .card__band { position: absolute; left: 0; top: 0; width: 543px; height: 318px; }

  .rig-art {
    position: absolute;
    left: 52px;
    top: 30px;
    width: 124px;
    height: 262px;
    background: linear-gradient(180deg, var(--teal-light) 0%, var(--teal) 45%, var(--yellow) 70%, var(--green) 100%);
    opacity: 0.55;
  }

  .holder {
    position: absolute;
    left: 253px;
    top: 40px;
  }
  .holder__name {
    margin: 0;
    font-family: "Michroma", sans-serif;
    font-size: 19px;
    font-weight: 400;
    color: var(--orange);
    line-height: 1.2;
    letter-spacing: 0.3px;
  }
  .holder__title {
    margin: 4px 0 0;
    font-family: "Roboto Condensed", sans-serif;
    font-size: 14px;
    color: var(--ink);
  }
  .contacts {
    position: absolute;
    left: 253px;
    top: 171px;
    margin: 0;
    padding: 0;
    list-style: none;
    font-family: "Roboto Condensed", sans-serif;
    font-size: 14px;
    color: var(--ink);
  }
  .contacts li {
    display: flex;
    align-items: center;
    height: 17.6px;
    white-space: nowrap;
  }
  .contacts svg { width: 13px; height: 13px; margin-right: 8px; flex: none; }

  .brand {
    position: absolute;
    left: 0;
    right: 0;
    top: 144px;
    display: flex;
    align-items: center;
    justify-content: center;
    gap: 14px;
  }
  .brand__mark { width: 28px; height: 28px; background: var(--orange); flex: none; }
  .brand__name {
    font-family: "Michroma", sans-serif;
    font-size: 21px;
    color: var(--teal);
    white-space: nowrap;
  }
</style>
</head>
<body>
<div class="canvas">

  <section class="card card--back" aria-label="Contact side">
    <svg class="card__band" viewBox="0 0 543 318" aria-hidden="true">
      <path d="M0 298 H352 C382 298 402 306 418 318 H0 Z" fill="var(--green)"/>
      <path d="M393 299 H543 V318 H430 C418 309 407 303 393 299 Z" fill="var(--orange)"/>
    </svg>

    <div class="rig-art" role="img" aria-label="Illustration of an oil derrick with a windsock"></div>

    <div class="holder">
      <h1 class="holder__name">Dale Harrow</h1>
      <p class="holder__title">Managing Director</p>
    </div>

    <ul class="contacts">
      <li>
        <svg viewBox="0 0 13 13"><rect width="13" height="13" rx="2" fill="var(--orange)"/><rect x="4" y="2" width="5" height="9" rx="1" fill="#fff"/><rect x="5" y="3" width="3" height="5" fill="var(--orange)"/></svg>
        +1 555.204.7719
      </li>
      <li>
        <svg viewBox="0 0 13 13"><rect width="13" height="13" rx="2" fill="var(--orange)"/><path d="M4 2.5 L5.5 2.5 L6 5 L5 6 C5.6 7.3 6.3 8 7 8.3 L8 7.3 L10.5 7.8 L10.5 9.5 C7 10.5 2.5 6 4 2.5 Z" fill="#fff"/></svg>
        +1 555.204.7719
      </li>
      <li>
        <svg viewBox="0 0 13 13"><rect width="13" height="13" rx="2" fill="var(--orange)"/><rect x="2.5" y="5" width="8" height="5.5" fill="#fff"/><rect x="4" y="2.5" width="5" height="3" fill="#fff"/></svg>
        +1 555.204.7719
      </li>
      <li>
        <svg viewBox="0 0 13 13"><rect width="13" height="13" rx="2" fill="var(--orange)"/><rect x="2.5" y="3.5" width="8" height="6" fill="#fff"/><path d="M2.5 3.5 L6.5 7 L10.5 3.5" fill="none" stroke="var(--orange)" stroke-width="1"/></svg>
        Dwayne@meridalewellsitesafety.com
      </li>
      <li>
        <svg viewBox="0 0 13 13"><rect width="13" height="13" rx="2" fill="var(--orange)"/><circle cx="6.5" cy="6.5" r="4" fill="none" stroke="#fff" stroke-width="1"/><path d="M2.5 6.5 H10.5 M6.5 2.5 C4.5 5 4.5 8 6.5 10.5 M6.5 2.5 C8.5 5 8.5 8 6.5 10.5" fill="none" stroke="#fff" stroke-width="0.8"/></svg>
        www.meridalewellsitesafety.com
      </li>
      <li>
        <svg viewBox="0 0 13 13"><rect width="13" height="13" rx="2" fill="var(--orange)"/><path d="M6.5 11 C4 8 3.5 6.5 3.5 5.5 A3 3 0 0 1 9.5 5.5 C9.5 6.5 9 8 6.5 11 Z" fill="#fff"/><circle cx="6.5" cy="5.5" r="1.2" fill="var(--orange)"/></svg>
        12 Kestrel Road, Ardmore, WA, 6301
      </li>
    </ul>
  </section>

  <section class="card card--front" aria-label="Brand side">
    <svg class="card__band" viewBox="0 0 543 318" aria-hidden="true">
      <path d="M0 298 H352 C382 298 402 306 418 318 H0 Z" fill="var(--green)"/>
      <path d="M393 299 H543 V318 H430 C418 309 407 303 393 299 Z" fill="var(--orange)"/>
    </svg>

    <div class="brand">
      <span class="brand__mark" aria-hidden="true"></span>
      <span class="brand__name">Meridale Wellsite &amp; Safety</span>
    </div>
  </section>

</div>
</body>
</html>
```